Brickwise Returns Online Redesign

The company needs a new online presence built that better represents who we are and what we do. Our online presence needs to be optimised for both PC, tablet and Phone usage.

Our existing site; www.brickwisereturns.com.au - this page currently forwards to one of our sales pages.
The entire site needs to be redesigned along with the sales pages /workshop and /faststart

Here are our competition:
https://www.celiamarwood.com/
http://quorvineacademy.com.au/learning-team/celia-marwood/
http://rosalindhetheridge.com.au/
www.makeoverventures.com.au/
http://bestlayoutsplaybook.com.au/

Target Market(s)

40-55 Husband and Wife with children that are busy profesionals with a family income of 150-300k PA with 2-3 kids

Industry/Entity Type

Education

Number of Pages Required

5+ page

Font styles to use
Sans Serif
Script

Colors

Designer to choose colors to be used in the design.

Requirements
Must have
• Main Page
• Events Page
• Media Page
• Past Projects
• Blog - plesae design a template blog; both individual blogs and library (i like this http://wexo.blog/)
• eBooks page
• Shopping Cart - buy eBooks, eBook Packs and courses
• eBook download page for each eBook
• Testimonials
• Event Sales Page
• 2 hr Event - currently www.brickwisereturns.com.au/workshop & /faststart & /faststartv
Nice to have
• A few different options for sales landing pages to sell the 2 hr event
• A few different blog templates - video, text, infographic etc
• The business is a Property Educatiom, Mentoring and Consulting Company
Should not have
• This is not a real estate sales business

```html
<!DOCTYPE html>
<html lang="en">
<head>
<meta charset="utf-8">
<title>Brickwise Returns</title>
<link href="https://fonts.googleapis.com/css2?family=Jost:wght@400;500;600&family=Open+Sans:wght@400;600;700&display=swap" rel="stylesheet">
<style>
:root{
  --orange:#e0901f;
  --orange-dark:#c97c12;
  --blue:#1b77bd;
  --blue-deep:#16609c;
  --navy:#1d3f7a;
  --ink:#222;
  --text:#555;
  --muted:#8a8a8a;
  --line:#dcdcdc;
  --pale:#f2f7fc;
  --white:#fff;
}
*{margin:0;padding:0;box-sizing:border-box}
html,body{width:1200px;height:2748px;overflow:hidden;background:var(--white)}
body{position:relative;font-family:"Open Sans",Arial,sans-serif;color:var(--text)}
.heading{font-family:"Jost","Century Gothic",sans-serif;color:var(--ink);font-weight:500;letter-spacing:.5px}
.btn-outline{position:absolute;border:2px solid #cfcfcf;border-radius:24px;color:var(--orange);font-weight:700;font-size:14px;display:flex;align-items:center;justify-content:center;text-transform:uppercase;background:var(--white)}
.btn-solid{position:absolute;background:var(--orange);border:2px solid #fff5;border-radius:24px;color:var(--white);font-weight:700;font-size:14px;display:flex;align-items:center;justify-content:center;text-transform:uppercase;box-shadow:0 2px 6px rgba(0,0,0,.2)}

/* header */
.site-header{position:absolute;left:0;top:0;width:1200px;height:82px;background:var(--white);z-index:3;box-shadow:0 1px 4px rgba(0,0,0,.12)}
.logo-badge{position:absolute;left:84px;top:-20px;width:188px;height:188px;border-radius:50%;background:var(--white);z-index:4;display:flex;align-items:center;justify-content:center;flex-direction:column;box-shadow:0 2px 6px rgba(0,0,0,.15)}
.logo-name{font-family:"Jost",sans-serif;font-weight:600;color:var(--navy);font-size:22px;line-height:1.05;text-align:center;margin-top:30px}
.nav{position:absolute;left:460px;top:32px;display:flex;gap:34px;font-size:14px;font-weight:600;color:var(--ink)}
.nav .active{color:var(--orange)}
.ask{position:absolute;left:920px;top:20px}
.ask small{display:block;font-size:12px;font-weight:600;color:var(--ink);margin-left:46px}
.ask strong{display:block;font-size:22px;color:var(--blue);margin-left:46px;margin-top:2px}
.ask .ring{position:absolute;left:0;top:4px;width:32px;height:32px;border:1px solid #ccc;border-radius:50%;display:flex;align-items:center;justify-content:center}

/* hero */
.hero{position:absolute;left:0;top:82px;width:1200px;height:468px;background:linear-gradient(180deg,#9db4c8 0%,#6d8ba5 35%,#4d6a80 65%,#3b5465 100%)}
.hero h1{position:absolute;left:0;width:1200px;top:118px;text-align:center;font-family:"Jost",sans-serif;font-weight:500;font-size:60px;color:var(--white);letter-spacing:1px;text-shadow:0 2px 6px rgba(0,0,0,.3)}
.hero p{position:absolute;left:0;width:1200px;top:196px;text-align:center;font-size:22px;font-weight:600;line-height:31px;color:var(--white);text-shadow:0 1px 4px rgba(0,0,0,.4)}
.dots{position:absolute;left:562px;top:412px;display:flex;gap:6px}
.dots i{width:12px;height:12px;border-radius:50%;border:2px solid var(--white)}
.dots i.on{background:var(--white)}

/* workshop */
.workshop h2{position:absolute;left:99px;top:620px;font-size:26px;line-height:37px;width:420px}
.workshop .copy{position:absolute;left:99px;top:708px;width:450px;font-size:12px;line-height:22px;color:var(--text)}
.video{position:absolute;left:599px;top:615px;width:503px;height:332px;border:1px solid #ddd;padding:5px;background:var(--white);box-shadow:0 1px 4px rgba(0,0,0,.1)}
.video .frame{width:100%;height:100%;background:linear-gradient(135deg,#3f6b46 0%,#5f8a5a 40%,#9ab0b8 70%,#c9d3d8 100%);position:relative}
.play{position:absolute;left:220px;top:130px;width:56px;height:56px;border-radius:50%;background:rgba(30,30,30,.85)}

/* topics */
.topics-photo{position:absolute;left:0;top:1017px;width:599px;height:405px;background:linear-gradient(120deg,#c8b59c 0%,#a98a69 40%,#8b6b4c 70%,#d8d0c4 100%)}
.topics-panel{position:absolute;left:599px;top:1017px;width:601px;height:405px;background:var(--pale)}
.topics-panel h2{position:absolute;left:77px;top:50px;font-size:26px}
.topics-list{position:absolute;left:77px;top:112px;list-style:none}
.topics-list li{display:flex;align-items:center;height:35px;font-size:12px;color:var(--text)}
.topics-list svg{margin-right:14px}

/* blog */
.blog h2{position:absolute;left:0;width:1200px;top:1494px;text-align:center;font-size:26px}
.card{position:absolute;top:1566px;width:323px}
.card .thumb{width:323px;height:211px;border:1px solid #ddd;padding:5px;background:var(--white);position:relative}
.card .thumb-img{width:100%;height:100%}
.card .date{position:absolute;left:-8px;top:138px;width:46px;height:62px;background:var(--orange);color:var(--white);text-align:center}
.card .date b{display:block;font-size:22px;line-height:30px;margin-top:4px}
.card .date span{display:block;font-size:11px;line-height:16px}
.card h3{font-size:18px;font-weight:600;color:var(--ink);line-height:25px;margin-top:28px;height:50px}
.card hr{border:0;border-top:1px solid var(--line);margin-top:17px}
.meta{display:flex;align-items:center;gap:6px;font-size:12px;color:var(--muted);margin-top:16px}
.meta svg{flex:none}
.meta .gap{width:16px}

/* instructors */
.instructors{position:absolute;left:0;top:1984px;width:1200px;height:409px;background:linear-gradient(160deg,var(--blue) 0%,#1a6fb2 50%,var(--blue-deep) 100%)}
.portrait{position:absolute;left:101px;top:57px;width:242px;height:242px;border-radius:50%;border:5px solid var(--white);background:linear-gradient(180deg,#e9eef2 0%,#c9d2da 50%,#2b3440 80%,#1f2630 100%)}
.instructors h2{position:absolute;left:416px;top:52px;color:var(--white);font-size:26px}
.bio{position:absolute;left:416px;width:700px;display:flex;font-size:12px;line-height:24px;color:var(--white)}
.bio b{width:141px;flex:none;font-weight:600}
.bio a{color:var(--orange);font-weight:700;text-decoration:none}

/* footer */
.foot-logo{position:absolute;left:99px;top:2500px;width:223px;text-align:center;display:flex;flex-direction:column;align-items:center}
.foot-logo .mark{width:38px;height:38px;border-radius:50%;background:var(--orange);margin-bottom:14px}
.foot-logo .name{font-family:"Jost",sans-serif;font-weight:600;color:var(--navy);font-size:34px;line-height:1.05}
.foot-col{position:absolute;top:2463px}
.foot-col h4{font-family:"Jost",sans-serif;font-weight:500;font-size:20px;color:var(--ink);margin-bottom:22px}
.foot-links{list-style:none;font-size:12px;line-height:27.5px;color:var(--text)}
.foot-col p{font-size:12px;line-height:20px;color:var(--text);width:250px}
.email-field{width:256px;height:36px;border:1px solid #ccc;margin-top:18px;font-size:12px;color:#aaa;padding:9px 12px}
.subscribe{position:relative;margin-top:16px;width:96px;height:32px;border:1px solid #ccc;border-radius:18px;color:var(--orange);font-size:11px;font-weight:700;display:flex;align-items:center;justify-content:center}
.contact-row{display:flex;align-items:center;font-size:12px;color:var(--text);height:51px}
.contact-row svg{margin-right:16px;flex:none}
.foot-rule{position:absolute;left:99px;top:2667px;width:1007px;border-top:1px solid var(--line)}
.copyright{position:absolute;left:99px;top:2696px;font-size:12px;color:var(--text)}
.social{position:absolute;left:944px;top:2687px;display:flex;gap:7px}
.social i{width:34px;height:34px;border-radius:50%;border:2px solid var(--blue)}
</style>
</head>
<body>

<header class="site-header">
  <nav class="nav">
    <span class="active">HOME</span><span>ABOUT</span><span>BLOG</span><span>EBOOK</span><span>CONTACT</span>
    <svg width="14" height="16" viewBox="0 0 14 16"><circle cx="6" cy="6" r="4.5" fill="none" stroke="#222" stroke-width="2"/><line x1="9.5" y1="9.5" x2="13" y2="13.5" stroke="#222" stroke-width="2"/></svg>
  </nav>
  <div class="ask">
    <span class="ring"><svg width="14" height="14" viewBox="0 0 24 24"><path d="M6.6 10.8c1.4 2.8 3.8 5.1 6.6 6.6l2.2-2.2c.3-.3.7-.4 1-.2 1.1.4 2.3.6 3.6.6.6 0 1 .4 1 1V20c0 .6-.4 1-1 1C10.6 21 3 13.4 3 4c0-.6.4-1 1-1h3.5c.6 0 1 .4 1 1 0 1.3.2 2.5.6 3.6.1.3 0 .7-.2 1z" fill="#e0901f"/></svg></span>
    <small>ASK A QUESTION</small>
    <strong>1300 415 927</strong>
  </div>
</header>
<div class="logo-badge"><div class="logo-name">BRICKWISE<br>RETURNS</div></div>

<section class="hero" role="img" aria-label="Aerial photograph of a harbour city skyline with bridge at dusk">
  <h1>BRICKWISE RETURNS</h1>
  <p>Make more money in 12 weeks Renovating Property than<br>most people make in 12 months in a job!</p>
  <div class="btn-solid" style="left:491px;top:286px;width:216px;height:42px">Book my seat now!</div>
  <div class="dots"><i class="on"></i><i></i><i></i><i></i></div>
</section>

<section class="workshop">
  <h2 class="heading">RENOVATING PROPERTY FOR<br>PROFIT WORKSHOP</h2>
  <div class="copy">
    <p>Book your seat now for only $29 to attend this LIVE Training Event so we can show you how we've Successfully Renovated 20 Properties for Profit in the last 3 years alone... and make more money in 12 weeks Renovating Property than most people make in 12 months in a job!</p>
    <p style="margin-top:22px">Event Details: Tuesday 2nd May 2017 at 7pm to 9pm - Harbourline Hotel Parramatta Sydney. Tickets only $29.</p>
  </div>
  <div class="btn-outline" style="left:99px;top:893px;width:198px;height:42px">Book my seat now!</div>
  <div class="video">
    <div class="frame" role="img" aria-label="Video still of a presenter standing in a tropical garden">
      <div class="play"><svg width="56" height="56" viewBox="0 0 56 56"><path d="M22 17l17 11-17 11z" fill="#fff"/></svg></div>
    </div>
  </div>
</section>

<div class="topics-photo" role="img" aria-label="Two builders in hard hats reviewing plans inside a renovation site"></div>
<section class="topics-panel">
  <h2 class="heading">WORKSHOP TOPICS</h2>
  <ul class="topics-list">
    <li><svg width="14" height="14" viewBox="0 0 14 14"><circle cx="7" cy="7" r="7" fill="#1b77bd"/><path d="M3.8 7.2l2.2 2.2 4.2-4.4" fill="none" stroke="#fff" stroke-width="1.8"/></svg>Recent Case Studies of Renovating for Profit</li>
    <li><svg width="14" height="14" viewBox="0 0 14 14"><circle cx="7" cy="7" r="7" fill="#1b77bd"/><path d="M3.8 7.2l2.2 2.2 4.2-4.4" fill="none" stroke="#fff" stroke-width="1.8"/></svg>Everybody can renovate, but can Everybody Renovate for Profit?</li>
    <li><svg width="14" height="14" viewBox="0 0 14 14"><circle cx="7" cy="7" r="7" fill="#1b77bd"/><path d="M3.8 7.2l2.2 2.2 4.2-4.4" fill="none" stroke="#fff" stroke-width="1.8"/></svg>Buying Houses in any Market and Renovate for Profit</li>
    <li><svg width="14" height="14" viewBox="0 0 14 14"><circle cx="7" cy="7" r="7" fill="#1b77bd"/><path d="M3.8 7.2l2.2 2.2 4.2-4.4" fill="none" stroke="#fff" stroke-width="1.8"/></svg>How to get Funding for your Project</li>
    <li><svg width="14" height="14" viewBox="0 0 14 14"><circle cx="7" cy="7" r="7" fill="#1b77bd"/><path d="M3.8 7.2l2.2 2.2 4.2-4.4" fill="none" stroke="#fff" stroke-width="1.8"/></svg>The Proven Property Renovation Step-by-Step Blueprint</li>
  </ul>
  <div class="btn-outline" style="left:81px;top:306px;width:196px;height:42px">View more topics</div>
</section>

<section class="blog">
  <h2 class="heading">LATEST BLOG</h2>
  <article class="card" style="left:97px">
    <div class="thumb"><div class="thumb-img" role="img" aria-label="Empty room with timber floor mid-renovation" style="background:linear-gradient(135deg,#6b4a30,#a77c55 50%,#d9c2a0)"></div><div class="date"><b>14</b><span>FEB</span></div></div>
    <h3>How I moved from full-time Teaching to Renovating Properties..</h3>
    <hr>
    <div class="meta"><svg width="11" height="12" viewBox="0 0 11 12"><circle cx="5.5" cy="3" r="3" fill="#1b77bd"/><path d="M0 12c0-4 2.5-5.5 5.5-5.5S11 8 11 12z" fill="#1b77bd"/></svg>Marcus Delane-Hart<span class="gap"></span><svg width="14" height="12" viewBox="0 0 14 12"><path d="M1 1h8v5H4l-2 2V6H1z" fill="none" stroke="#1b77bd" stroke-width="1.3"/><path d="M10 4h3v5h-1v2l-2-2H6V7" fill="none" stroke="#1b77bd" stroke-width="1.3"/></svg>3 Comments</div>
  </article>
  <article class="card" style="left:441px">
    <div class="thumb"><div class="thumb-img" role="img" aria-label="Three people discussing plans in a bright room under renovation" style="background:linear-gradient(135deg,#c9a77e,#e7dccb 50%,#8d7259)"></div><div class="date"><b>01</b><span>JAN</span></div></div>
    <h3>7 tips to reduce risk when renovating for profit</h3>
    <hr>
    <div class="meta"><svg width="11" height="12" viewBox="0 0 11 12"><circle cx="5.5" cy="3" r="3" fill="#1b77bd"/><path d="M0 12c0-4 2.5-5.5 5.5-5.5S11 8 11 12z" fill="#1b77bd"/></svg>Marcus Delane-Hart<span class="gap"></span><svg width="14" height="12" viewBox="0 0 14 12"><path d="M1 1h8v5H4l-2 2V6H1z" fill="none" stroke="#1b77bd" stroke-width="1.3"/><path d="M10 4h3v5h-1v2l-2-2H6V7" fill="none" stroke="#1b77bd" stroke-width="1.3"/></svg>3 Comments</div>
  </article>
  <article class="card" style="left:786px">
    <div class="thumb"><div class="thumb-img" role="img" aria-label="Couple looking at a laptop among moving boxes" style="background:linear-gradient(135deg,#e9d9c6,#c49a72 50%,#f3ede4)"></div><div class="date"><b>28</b><span>JAN</span></div></div>
    <h3>How To Attain Financial Freedom Through Renovating</h3>
    <hr>
    <div class="meta"><svg width="11" height="12" viewBox="0 0 11 12"><circle cx="5.5" cy="3" r="3" fill="#1b77bd"/><path d="M0 12c0-4 2.5-5.5 5.5-5.5S11 8 11 12z" fill="#1b77bd"/></svg>Marcus Delane-Hart<span class="gap"></span><svg width="14" height="12" viewBox="0 0 14 12"><path d="M1 1h8v5H4l-2 2V6H1z" fill="none" stroke="#1b77bd" stroke-width="1.3"/><path d="M10 4h3v5h-1v2l-2-2H6V7" fill="none" stroke="#1b77bd" stroke-width="1.3"/></svg>3 Comments</div>
  </article>
</section>

<section class="instructors">
  <div class="portrait" role="img" aria-label="Portrait of the two workshop instructors in suits"></div>
  <h2 class="heading" style="color:#fff">WORKSHOP INSTRUCTORS</h2>
  <div class="bio" style="top:116px"><b>Warren Pelham:</b><span>In 1984, at just 19 years old, I began investing in property. Over the course of the past 30 years, I've invested more than $250,000 in personal development, property seminars and programs with experts in their respective fields. <a>READ MORE &gt;&gt;</a></span></div>
  <div class="bio" style="top:212px"><b>Marcus Delane-Hart:</b><span>I began investing in property in 2001, when I was 25 years old. During the past 10 years, I have invested $100,000 in personal development and property seminar programs with the top people in the field of wealth creation. <a>READ MORE &gt;&gt;</a></span></div>
  <div class="btn-solid" style="left:416px;top:315px;width:201px;height:42px">Book my seat now!</div>
</section>

<footer>
  <div class="foot-logo"><span class="mark"></span><span class="name">BRICKWISE<br>RETURNS</span></div>
  <div class="foot-col" style="left:387px">
    <h4>Information</h4>
    <ul class="foot-links"><li>Home</li><li>About</li><li>Blog</li><li>Ebook</li><li>Contact</li></ul>
  </div>
  <div class="foot-col" style="left:573px">
    <h4>Newsletter Subscription</h4>
    <p>Register your Email Address to get information about us</p>
    <div class="email-field">Email Address</div>
    <div class="subscribe">SUBSCRIBE</div>
  </div>
  <div class="foot-col" style="left:885px">
    <h4>Contact Us</h4>
    <div class="contact-row" style="margin-top:-14px"><svg width="11" height="15" viewBox="0 0 11 15"><path d="M5.5 0C2.5 0 0 2.4 0 5.4 0 9.5 5.5 15 5.5 15S11 9.5 11 5.4C11 2.4 8.5 0 5.5 0zm0 7.5a2 2 0 110-4 2 2 0 010 4z" fill="#1b77bd"/></svg>Harbourline Hotel Parramatta</div>
    <div class="contact-row"><svg width="13" height="13" viewBox="0 0 24 24"><path d="M6.6 10.8c1.4 2.8 3.8 5.1 6.6 6.6l2.2-2.2c.3-.3.7-.4 1-.2 1.1.4 2.3.6 3.6.6.6 0 1 .4 1 1V20c0 .6-.4 1-1 1C10.6 21 3 13.4 3 4c0-.6.4-1 1-1h3.5c.6 0 1 .4 1 1 0 1.3.2 2.5.6 3.6.1.3 0 .7-.2 1z" fill="#1b77bd"/></svg>1300 415 927</div>
    <div class="contact-row"><svg width="14" height="11" viewBox="0 0 14 11"><rect width="14" height="11" rx="1" fill="#1b77bd"/><path d="M1 1.5l6 4.5 6-4.5" fill="none" stroke="#fff" stroke-width="1.2"/></svg>info@brickwisereturns.com.au</div>
  </div>
  <div class="foot-rule"></div>
  <div class="copyright">Copyright © 2017, Brickwise Returns. All rights reserved.</div>
  <div class="social"><i></i><i></i><i></i><i></i></div>
</footer>

</body>
</html>
```